" O escritório Brunoro Arquitetura desenvolve projetosarquitetônicos e interiores, além de acompanhamento e administraçãao de obras. Tem a frente de sua gestão a arquiteta Mariana Forteso, que prioriza o atendimento exclusivo e diferenciado a cada um dos clientes, estabelecendo assim uma relação de proximidade, confiança e fidelização. Todos os projetos são desenvolvidos de acordo com o perfil do cliente, buscando sempre soluções inovadoras, criativas e acessíveis, em muitos casos utilizando materiais e soluções alternativas ao convencional, marca do escritório. O espaço físico do escritório reflete essa proposta de inovação e criatividade, que permite a acessibilidade da arquitetura a qualquer pessoa, desmistificando o status de que a boa arquitetura é acessível somente àqueles que possuem um alto poder aquisitivo. Todo o processo de concepção e posterior execução dos trabalhos é realizada entre os profissionais envolvidos e os clientes com total transparência, sendo a política de trabalho do escritório focada na ética, honestidade e respeito ao cliente, não havendo portanto o recebimento de reservas técnicas ou comissões de lojistas e empresas terceiras, para indicação de produtos. Assim, trabalhamos com total liberdade na concepção e especificação de materiais e soluções nos projetos. O escritório também tem ligação forte com as escolas de arquitetura da cidade, sendo um local de estágio e constante aprendizado para estudantes, que adquirem experiência profissional junto aos membros do escritório. A linguagem dos projetos, que deve se refletir na identidade visual da marca, busca a simplicidade dos materiais e formas, aplicadas da forma correta, gerando resultados simples, porém sofisticados. Priorizamos o uso dos materiais naturais em todos os projetos, mas prioritariamente o uso da madeira natural. Trabalhamos sempre com muito respeito pela história dos lugares, procurando sempre que possível preservar características originais que dão identidade aos lugares. "

```html
<!DOCTYPE html>
<html lang="pt-BR">
<head>
<meta charset="UTF-8">
<title>Brunoro Arquitetura — Cartão de Visita</title>
<link href="https://fonts.googleapis.com/css2?family=Mulish:wght@300;400&display=swap" rel="stylesheet">
<style>
  :root {
    --page-bg: #e4e5e6;
    --card-front: #ffffff;
    --card-back: #6c6f71;
    --ink-dark: #55585b;
    --ink-light: #eceded;
    --ink-soft: #d9dadb;
    --shadow: rgba(0, 0, 0, 0.14);
  }
  * { box-sizing: border-box; margin: 0; padding: 0; }
  html, body {
    width: 1200px;
    height: 1200px;
    overflow: hidden;
    background: var(--page-bg);
    font-family: "Mulish", "Helvetica Neue", Arial, sans-serif;
    font-weight: 300;
  }
  .canvas {
    position: relative;
    width: 1200px;
    height: 1200px;
  }
  .card {
    position: absolute;
    left: 160px;
    width: 880px;
    height: 503px;
    box-shadow: 0 10px 28px var(--shadow);
  }
  /* Front side */
  .card--front {
    top: 70px;
    background: var(--card-front);
    color: var(--ink-dark);
  }
  .front-mark {
    position: absolute;
    top: 150px;
    left: 0;
    right: 0;
    display: flex;
    flex-direction: column;
    align-items: center;
    gap: 22px;
  }
  .front-mark__square {
    width: 64px;
    height: 64px;
    border: 3px solid var(--ink-dark);
  }
  .front-mark__name {
    font-size: 34px;
    letter-spacing: 0.32em;
    text-transform: uppercase;
    padding-left: 0.32em;
  }
  .front-web {
    position: absolute;
    left: 0;
    right: 0;
    bottom: 62px;
    text-align: center;
    font-size: 19px;
    letter-spacing: 0.04em;
  }
  /* Back side */
  .card--back {
    top: 627px;
    background: var(--card-back);
    color: var(--ink-light);
  }
  .back-mark {
    position: absolute;
    top: 92px;
    left: 70px;
    display: flex;
    flex-direction: column;
    align-items: center;
    gap: 14px;
  }
  .back-mark__square {
    width: 52px;
    height: 52px;
    border: 2px solid var(--ink-light);
  }
  .back-mark__name {
    font-size: 36px;
    letter-spacing: 0.3em;
    text-transform: uppercase;
    line-height: 1.15;
    text-align: center;
  }
  .back-mark__name span { display: block; }
  .holder {
    position: absolute;
    top: 70px;
    right: 66px;
    text-align: right;
  }
  .holder__name {
    font-size: 27px;
    letter-spacing: 0.02em;
  }
  .holder__register {
    margin-top: 6px;
    font-size: 22px;
  }
  .address {
    position: absolute;
    top: 200px;
    right: 66px;
    text-align: right;
    font-size: 21px;
    line-height: 1.3;
  }
  .contact {
    position: absolute;
    left: 150px;
    bottom: 70px;
    text-align: right;
    font-size: 21px;
    line-height: 1.55;
  }
  .contact__label { color: var(--ink-soft); }
</style>
</head>
<body>
  <main class="canvas">
    <section class="card card--front" aria-label="Frente do cartão">
      <div class="front-mark">
        <div class="front-mark__square"></div>
        <div class="front-mark__name">Brunoro</div>
      </div>
      <p class="front-web">www.brunoroarq.com.br</p>
    </section>

    <section class="card card--back" aria-label="Verso do cartão">
      <div class="back-mark">
        <div class="back-mark__square"></div>
        <div class="back-mark__name"><span>Brunoro</span><span>Arquitetura</span></div>
      </div>

      <div class="holder">
        <p class="holder__name">Mariana Forteso</p>
        <p class="holder__register">CAU - 54810-27</p>
      </div>

      <address class="address" style="font-style: normal;">
        Rua das Acácias, 845<br>
        Bairro: Centro | CEP: 04512-330<br>
        São Paulo/SP
      </address>

      <div class="contact">
        <p><span class="contact__label">Telefones:</span> (11) 3456-7810 | (11) 98765-4321</p>
        <p>contato@brunoroarq.com.br</p>
      </div>
    </section>
  </main>
</body>
</html>
```